Banner & also another minor digital image for an Online Academic Journal

A direct example of what I need can be found in this webpage: http://papers.tbhu-archive.org/qrvt/
(Please see attached files, "sAMPLE", and "sAMPLE 2", so you can see what I mean.)
This link (http://papers.tbhu-archive.org/qrvt/) is for an existing ONLINE ACADEMIC JOURNAL at the Thornbury Hill University.
It will help for you to be acquainted with the format of Online Academic Journals.
You will find that there is a banner on top as well as a digital image of a journal/book cover on the right.
I need a
(1) banner and
a (2) digital journal/book cover
for a website for an ONLINE ACADEMIC JOURNAL.
I am looking for a serious, professional, elegant design.
There will not be a print version. Only web-based online publication. No coding needed, only PSD, JPG/PNG and PDF.
1) We use PelloWave (http://archives.pellowave.com/repository-software/journals/) for the digital image of the journal/book cover layout. Link shows the general layout of the journal website.
2) For the digital image of the journal/book cover and also the banner,
Name of the journal is....
"Lumen: A Quarterly of Civic Ethics and Recovery Work"
Only this text will be used and applied to both banner and cover.
***The color associated with the theme of dignity is purple
****You could also add the color red.
*****I don't want the design to be garish, but accents in red might represent
the sexual exploitation and violence in the title.
3) Attached "sAmple 2" file is a basic design for the digital image of the journal/book cover from PelloWave. I am looking for something more elegant and professional looking. Your creativity is encouraged. I am open to receiving your interpretation.
Target Market(s)
Academics & Community Professionals
Industry/Entity Type
Non Profit
Contact Information for Business Card
Match journal design

```html
<!DOCTYPE html>
<html lang="en">
<head>
<meta charset="utf-8">
<title>Lumen – Banner and Journal Cover</title>
<link href="https://fonts.googleapis.com/css2?family=Arimo:ital,wght@0,400;0,700;1,400&family=Tinos:wght@700&display=swap" rel="stylesheet">
<style>
  :root {
    --page-bg: #1c1828;
    --page-bg-deep: #120f1c;
    --sidebar: #1f1b33;
    --sidebar-text: #9d9ab0;
    --sidebar-rule: #3a3552;
    --content: #d3d3d3;
    --content-text: #444;
    --link: #3d4f8c;
    --heading: #2e2e2e;
    --purple: #5e3d8f;
    --purple-dark: #4a2d76;
    --banner-dark: #2a2a2c;
    --banner-black: #141414;
    --frame: #c9c9c9;
    --cover-frame: #0d0d0d;
    --follow: #2f7fc4;
    --footer: #15121f;
    --arrow-fill: rgba(255,255,255,0.82);
    --arrow-stroke: #111;
    --white: #fff;
  }
  * { box-sizing: border-box; margin: 0; padding: 0; }
  html, body { width: 1200px; height: 876px; overflow: hidden; }
  body {
    position: relative;
    background: linear-gradient(180deg, var(--page-bg) 0%, var(--page-bg-deep) 100%);
    font-family: "Arimo", Arial, sans-serif;
  }
  .abs { position: absolute; }

  /* Banner */
  .banner-frame {
    left: 58px; top: 17px; width: 1084px; height: 157px;
    border: 4px solid var(--frame); border-radius: 26px; overflow: hidden;
    background: linear-gradient(90deg, var(--banner-black) 0%, var(--banner-dark) 55%, #3a3a3c 100%);
  }
  .banner-name {
    left: 52px; top: 14px;
    font-family: "Arimo", Arial, sans-serif; font-weight: 400;
    font-size: 78px; line-height: 1; color: var(--white);
  }
  .banner-subtitle {
    left: 54px; top: 106px;
    font-family: "Arimo", Arial, sans-serif; font-weight: 400;
    font-size: 19px; line-height: 1; color: var(--white);
  }
  .banner-rule { left: 0; right: 0; bottom: 0; height: 10px; background: var(--purple); }
  .banner-photo {
    left: 618px; top: 0; width: 360px; height: 143px;
    background: radial-gradient(ellipse at 45% 55%, #b8b4b4 0%, #6c6868 35%, rgba(40,40,40,0) 72%);
  }

  /* Page */
  .sidebar { left: 78px; top: 195px; width: 253px; height: 641px; background: var(--sidebar); }
  .content { left: 331px; top: 195px; width: 786px; height: 641px; background: var(--content); }
  .nav { list-style: none; padding: 30px 0 0 12px; }
  .nav li { font-size: 12px; color: var(--sidebar-text); height: 25px; }
  .nav-group { border-top: 1px solid var(--sidebar-rule); margin-top: 12px; padding-top: 20px; }
  .nav-group li { height: 38px; }
  .side-label { font-size: 11.5px; color: var(--sidebar-text); left: 12px; }
  .field { left: 12px; height: 18px; background: #c8c8cc; border: 1px solid #888; font-size: 11px; color: #333; padding: 1px 4px; }
  .pill { height: 18px; background: #bdbdc2; border: 1px solid #777; border-radius: 9px; font-size: 10.5px; color: #222; padding: 1px 8px; }
  .side-heading { font-size: 12.5px; font-weight: 700; color: #bcb9cc; left: 12px; }

  .crumb { left: 46px; top: 30px; font-size: 11.5px; color: #666; }
  .crumb span { color: var(--link); }
  .follow { left: 703px; top: 75px; width: 50px; height: 20px; background: var(--follow); border-radius: 3px; color: var(--white); font-size: 11px; text-align: center; line-height: 20px; }
  .intro { left: 46px; top: 128px; width: 434px; font-size: 11.5px; line-height: 16px; color: var(--content-text); }
  .intro em { font-weight: 700; }
  .intro .inline-link { color: var(--link); text-decoration: underline; }
  .issue-title { left: 46px; top: 296px; font-size: 26px; color: var(--heading); }
  .articles-head { left: 46px; top: 341px; width: 428px; font-size: 22px; color: var(--heading); border-bottom: 1px solid #aaa; padding-bottom: 4px; }
  .article { left: 46px; font-size: 12.5px; }
  .article .pdf { display: inline-flex; align-items: center; gap: 3px; color: #666; font-size: 10.5px; width: 50px; }
  .article .name { color: var(--link); }
  .article .author { display: block; margin-left: 50px; font-style: italic; color: #444; font-size: 12px; }
  .editors-head { left: 520px; top: 472px; font-size: 17px; color: var(--heading); }
  .editor-role { left: 520px; font-size: 12px; color: #444; }
  .editor-name { left: 520px; font-size: 12px; font-weight: 700; color: #333; }

  .footer { left: 78px; top: 836px; width: 1039px; height: 40px; background: var(--footer); }
  .footer-brand { left: 20px; top: 7px; display: flex; align-items: center; gap: 6px; color: #cfcfd6; font-size: 14px; font-weight: 700; letter-spacing: 1px; }
  .footer-brand i { width: 10px; height: 10px; background: #cfcfd6; border-radius: 50%; display: block; }
  .footer-links { left: 299px; top: 23px; font-size: 11px; color: #ddd; word-spacing: 4px; }

  /* Cover */
  .cover-frame {
    left: 832px; top: 291px; width: 277px; height: 374px;
    border: 5px solid var(--cover-frame); border-radius: 24px; overflow: hidden;
    background: linear-gradient(180deg, #3a3a3a 0%, #1d1d1d 100%);
  }
  .cover-photo { left: 0; top: 0; width: 100%; height: 186px; background: radial-gradient(ellipse at 45% 40%, #c4bcbc 0%, #777 35%, #333 75%); }
  .cover-rule { left: 0; top: 186px; width: 100%; height: 10px; background: linear-gradient(90deg, var(--purple) 0%, var(--purple-dark) 100%); }
  .cover-name {
    left: 0; top: 214px; width: 100%; text-align: center;
    font-family: "Arimo", Arial, sans-serif; font-weight: 400;
    font-size: 62px; line-height: 1; color: var(--white);
  }
  .cover-subtitle {
    left: 0; top: 300px; width: 100%; text-align: center;
    font-family: "Arimo", Arial, sans-serif; font-weight: 400;
    font-size: 14px; line-height: 20px; color: var(--white);
  }

  /* Annotation arrows */
  .arrows { left: 0; top: 0; }
  .arrow-label { font-family: "Tinos", "Times New Roman", serif; font-weight: 700; text-decoration: underline; fill: #1a1a1a; }
</style>
</head>
<body>

<header class="abs banner-frame">
  <div class="abs banner-photo" role="img" aria-label="Photograph of a pale, desaturated rose lying on its side"></div>
  <h1 class="abs banner-name">Lumen</h1>
  <p class="abs banner-subtitle">A Quarterly of Civic Ethics and Recovery Work</p>
  <div class="abs banner-rule"></div>
</header>

<aside class="abs sidebar">
  <ul class="nav">
    <li>Journal Home</li>
    <li>About this Journal</li>
    <li>Aims &amp; Scope</li>
    <li>Editorial Board</li>
    <li>Policies</li>
  </ul>
  <ul class="nav nav-group">
    <li>Submit Articles</li>
    <li>Most Popular Papers</li>
    <li>Receive Email Notices or RSS</li>
  </ul>
  <p class="abs side-label" style="top:330px;">Select an Issue:</p>
  <div class="abs field" style="top:352px;width:146px;">All Issues ▾</div>
  <div class="abs pill" style="left:166px;top:352px;">Browse</div>
  <p class="abs side-heading" style="top:408px;">Search</p>
  <p class="abs side-label" style="top:430px;">Enter search terms:</p>
  <div class="abs field" style="top:452px;width:146px;"></div>
  <div class="abs pill" style="left:166px;top:452px;">Search</div>
  <div class="abs field" style="top:477px;width:146px;">in this journal ▾</div>
  <p class="abs side-label" style="top:525px;">Advanced Search</p>
</aside>

<main class="abs content">
  <p class="abs crumb">Home › <span>lumen</span></p>
  <div class="abs follow">Follow</div>
  <p class="abs intro"><em>Lumen: A Quarterly of Civic Ethics and Recovery Work</em> journal lorem ipsum dolor sit amet, consectetur adipiscing elit. Ut et justo ipsum elit, at tempus augue. Proin varius luctus elit, non ornare enim ultrices sit amet. Aliquam at enim nulla. Duis varius lacus in <span class="inline-link">dignissim</span> felis. Vivamus quam justo, tristique sit amet dignissim in, fermentum eu massa. Pellentesque egestas viverra est, sed volutpat neque scelerisque ac. <span class="inline-link">Class</span> aptent taciti sociosqu ad litora torquent per conubia nostra, per inceptos himenaeos.</p>
  <h2 class="abs issue-title">Volume #, Issue # (YYYY) Issue Title</h2>
  <h3 class="abs articles-head">Articles</h3>

  <div class="abs article" style="top:396px;"><span class="pdf"><svg width="11" height="12" viewBox="0 0 11 12"><path d="M2 11 L5 1 L7 6 L10 10 Z" fill="none" stroke="#c0392b" stroke-width="1.4"/></svg>PDF</span><span class="name">Name of Article Here</span><span class="author">Name of Author</span></div>
  <div class="abs article" style="top:454px;"><span class="pdf"><svg width="11" height="12" viewBox="0 0 11 12"><path d="M2 11 L5 1 L7 6 L10 10 Z" fill="none" stroke="#c0392b" stroke-width="1.4"/></svg>PDF</span><span class="name">Name of Article Here</span><span class="author">Name of Author</span></div>
  <div class="abs article" style="top:512px;"><span class="pdf"><svg width="11" height="12" viewBox="0 0 11 12"><path d="M2 11 L5 1 L7 6 L10 10 Z" fill="none" stroke="#c0392b" stroke-width="1.4"/></svg>PDF</span><span class="name">Name of Article Here</span><span class="author">Name of Author</span></div>
  <div class="abs article" style="top:570px;"><span class="pdf"><svg width="11" height="12" viewBox="0 0 11 12"><path d="M2 11 L5 1 L7 6 L10 10 Z" fill="none" stroke="#c0392b" stroke-width="1.4"/></svg>PDF</span><span class="name">Name of Article Here</span><span class="author">Name of Author</span></div>

  <h3 class="abs editors-head">Editors</h3>
  <p class="abs editor-role" style="top:533px;">Editor-in-Chief</p>
  <p class="abs editor-name" style="top:556px;">Name Here</p>
  <p class="abs editor-role" style="top:589px;">Managing Editor</p>
  <p class="abs editor-name" style="top:612px;">Name Here</p>
</main>

<footer class="abs footer">
  <div class="abs footer-brand"><i></i>SCHOLAR VAULT</div>
  <p class="abs footer-links">Home | About | FAQ | My Account | Accessibility Statement</p>
</footer>

<section class="abs cover-frame" aria-label="Journal cover">
  <div class="abs cover-photo" role="img" aria-label="Photograph of a pale, desaturated rose on a dark ground"></div>
  <div class="abs cover-rule"></div>
  <h2 class="abs cover-name">Lumen</h2>
  <p class="abs cover-subtitle">A Quarterly of<br>Civic Ethics and Recovery Work</p>
</section>

<svg class="abs arrows" width="1200" height="876" viewBox="0 0 1200 876" aria-hidden="true">
  <path d="M718 185 L843 290 L775 290 L775 389 L659 389 L659 290 L592 290 Z" fill="var(--arrow-fill)" stroke="var(--arrow-stroke)" stroke-width="2.5" stroke-linejoin="miter"/>
  <path d="M497 444 L679 444 L679 406 L844 468 L679 530 L679 497 L497 497 Z" fill="var(--arrow-fill)" stroke="var(--arrow-stroke)" stroke-width="2.5" stroke-linejoin="miter"/>
  <text x="660" y="267" class="arrow-label" font-size="19">#2 Banner</text>
  <text x="508" y="470" class="arrow-label" font-size="19">#1 Journal/Book Cover</text>
</svg>

</body>
</html>
```